Gerald Pinnock - Corporate MC & Entertainer

Design a one page A4 flyer
(See Brief Attached)
I'm after a one Page Flyer
A4 Size - One sided
I want the finished artwork in 2 Forms.
1/ One that I could print out myself in a small run ( I have a Dorvan Tint PrintMaster)
or send out as a PDF
2/ A second version that could be printed commercially , so including bleed crop marks so it can be cut to A4 size
I have attached the copy that should be included. (Agency Sweep 2014 WORDS)
If there was too much text to include , we could drop one of the testimonial quotes
I have attached 3 images that could be included if there is room.
If there were too many images I suggest dropping Image 3 ( with bow tie)
As you can see from the copy (or a visit to my website) there are two main services that I provide
Corporate MC Services and Entertainment Services.
These are however intertwined - My MC work often includes some entertaining effects from my ThoughtCatcher Show. I often get booked to MC a conference and provide a show.
I'm after something that is -
Classy , Sophisticated, Smart, perhaps a bit quirky.
Nothing "Magic" like - eg no Rabbits , Wands, puffs of smoke
I have no corporate colour or logo or branding that should be included
You can see some previous flyers here http://www.proflinkora.com/in/geraldpinnock
I like these, but looking for new ideas
Target Market(s)
Corporate , Conference Organisers, Speaker Bureau owners, Large Association Conference committees
Industry/Entity Type
Entertainment
Colors
Designer to choose colors to be used in the design.

```html
<!DOCTYPE html>
<html lang="en">
<head>
<meta charset="utf-8">
<title>Gerald Pinnock – Corporate MC &amp; Entertainer</title>
<link href="https://fonts.googleapis.com/css2?family=Archivo+Black&family=Roboto+Condensed:ital,wght@0,400;0,700;1,700&family=Playfair+Display:wght@400&display=swap" rel="stylesheet">
<style>
  :root {
    --page-bg: #e9e6e1;
    --ink-black: #121212;
    --panel-dark: #1d1d1d;
    --gold-light: #f6d45a;
    --gold: #f0b43a;
    --orange: #e8872e;
    --white: #ffffff;
    --body-grey: #e6e6e6;
    --band-yellow: #f2d36a;
    --band-deep: #e8b94a;
    --text-dark: #1a1a1a;
  }
  * { box-sizing: border-box; margin: 0; padding: 0; }
  html, body { width: 1200px; height: 1000px; overflow: hidden; }
  body {
    background: var(--page-bg);
    font-family: "Roboto Condensed", Arial, sans-serif;
    position: relative;
  }
  .flyer {
    position: absolute;
    left: 270px; top: 33px;
    width: 660px; height: 934px;
    background: var(--ink-black);
    overflow: hidden;
    box-shadow: 0 6px 24px rgba(0,0,0,.25);
  }
  .hero {
    position: absolute; left: 0; top: 0; width: 660px; height: 380px;
  }
  .hero__backdrop {
    position: absolute; inset: 0;
    background: linear-gradient(160deg, #2a2a2a 0%, #3b3b3b 45%, #161616 100%);
  }
  .hero__portrait {
    position: absolute; left: 40px; top: 30px; width: 300px; height: 350px;
    background: radial-gradient(ellipse at 55% 35%, #8c8c8c 0%, #3f3f3f 50%, #1c1c1c 100%);
  }
  .name {
    position: absolute; left: 345px; top: 70px;
    font-family: "Archivo Black", Arial, sans-serif;
    font-size: 64px; line-height: 0.95;
    transform: skewX(-10deg);
    background: linear-gradient(180deg, var(--gold-light) 0%, var(--gold) 50%, var(--orange) 100%);
    -webkit-background-clip: text; background-clip: text;
    color: transparent;
  }
  .headline {
    position: absolute; left: 0; top: 305px; width: 660px; text-align: center;
  }
  .headline__country {
    font-family: "Archivo Black", Arial, sans-serif;
    font-size: 66px; color: var(--white); letter-spacing: 1px;
    line-height: 1;
  }
  .headline__title {
    font-family: "Playfair Display", Georgia, serif;
    font-size: 48px; color: var(--orange);
    margin-top: -26px; line-height: 1;
  }
  .tagline {
    position: absolute; left: 0; top: 420px; width: 660px; text-align: center;
    font-weight: 700; font-style: italic; font-size: 19px; color: var(--white);
  }
  .rule {
    position: absolute; left: 40px; top: 452px; width: 580px; height: 2px;
    background: #8a8a8a;
  }
  .bio {
    position: absolute; left: 55px; top: 468px; width: 550px;
    text-align: center; color: var(--body-grey);
    font-size: 13.5px; line-height: 1.35;
  }
  .bio p { margin-bottom: 7px; }
  .cta {
    position: absolute; left: 0; top: 640px; width: 660px; text-align: center;
  }
  .cta__question {
    font-family: "Archivo Black", Arial, sans-serif;
    font-size: 32px; color: var(--white);
  }
  .cta__link {
    font-weight: 700; font-size: 22px; color: var(--orange);
  }
  .testimonials {
    position: absolute; left: 0; bottom: 0; width: 660px; height: 190px;
    background: linear-gradient(180deg, var(--band-yellow) 0%, var(--band-deep) 100%);
    padding: 18px 40px 0;
    color: var(--text-dark);
  }
  .testimonials__heading {
    font-weight: 700; font-size: 17px;
    border-bottom: 2px solid var(--text-dark);
    padding-bottom: 5px; margin-bottom: 10px;
  }
  .testimonials__quote {
    font-size: 12.5px; line-height: 1.35; margin-bottom: 8px;
  }
  .testimonials__source { font-weight: 700; }
</style>
</head>
<body>
  <article class="flyer">
    <section class="hero">
      <div class="hero__backdrop" role="img" aria-label="Dark city skyscrapers with a conference microphone"></div>
      <div class="hero__portrait" role="img" aria-label="Portrait of Gerald Pinnock in a dark suit, pointing and smiling"></div>
      <h1 class="name">Gerald<br>Pinnock</h1>
      <div class="headline">
        <div class="headline__country">AUSTRALIA'S</div>
        <div class="headline__title">Magician of the Mind</div>
      </div>
    </section>

    <p class="tagline">Corporate MC &amp; Entertainer. Solving your Conference Puzzles!</p>
    <div class="rule"></div>

    <div class="bio">
      <p>In the last two years Gerald has been engaged as the Conference MC for events in Hawaii, New Zealand, Hong Kong &amp; all States of Australia.</p>
      <p>He facilitated 24 Australian Major Project Conferences for ConvexaTrade and 16 International CEO Summits for Halvern Global.</p>
      <p>In the Australian Corporate Sector, he managed major events for – Meridale Brokers, NBQA, Homefold Care, Vantel Rentals, Brightwell Care and the Plant &amp; Grower Association.</p>
      <p>As an Entertainer he cruised the world on several luxury cruise ships, visiting Japan, Korea, China, Tahiti and New Zealand in his travels.</p>
    </div>

    <div class="cta">
      <div class="cta__question">What's coming up in 2014?</div>
      <div class="cta__link">Get involved at http://www.GeraldPinnockLive.com</div>
    </div>

    <section class="testimonials">
      <h2 class="testimonials__heading">Recent Testimonials</h2>
      <p class="testimonials__quote">"A big thank you for a really good job on Friday night which was carried out with aplomb - well done!" – <span class="testimonials__source">Plant &amp; Grower Association</span></p>
      <p class="testimonials__quote">"Huge thanks for your professionalism with the Awards, getting a laugh from everyone and in general creating an atmosphere that was enjoyable and relaxed!" – <span class="testimonials__source">Homefold Care</span></p>
    </section>
  </article>
</body>
</html>
```